New Update: I am changing the title of the book and the back cover text. Title was too long before. Same style as before.
New Title: Under the Quiet Sky
New Subtitle: A Gardener’s Notes on Patience (italics on front cover)

Back cover text:
Under the Quiet Sky: A Gardener’s Notes on Patience offers clear, compassionate guidance for those recovering from total loss. Drawing from his experience as a Brennick Flood survivor, Tobias Quellhorst shares practical advice on insurance, rebuilding, and emotional healing, along with lessons in strength and community. This is not a book about tragedy; it’s about perseverance and renewal. Under the Quiet Sky is a trusted companion for anyone rebuilding life, home, and hope after disaster.

Font styles to use
Serif

Colors
EB3D1F
EC4F4E
F09395
F8D3D4
FCEDEE

Requirements
Should not have
• No pictures or anything related to fire on the cover.

```html
<!DOCTYPE html>
<html lang="en">
<head>
<meta charset="utf-8">
<title>Under the Quiet Sky — Front Cover</title>
<link href="https://fonts.googleapis.com/css2?family=EB+Garamond:wght@400;500&family=Cormorant+Garamond:ital,wght@1,500&display=swap" rel="stylesheet">
<style>
  :root {
    --page: #ffffff;
    --cover-edge: #461216;
    --cover-mid: #6a1519;
    --cover-glow: #a11a1f;
    --ink-cream: #fdf1dc;
    --rule-gold: #d9a21c;
    --sketch-tint: rgba(248, 211, 212, 0.10);
  }
  html, body {
    margin: 0;
    width: 1200px;
    height: 1200px;
    overflow: hidden;
    background: var(--page);
  }
  .canvas {
    position: relative;
    width: 1200px;
    height: 1200px;
  }
  .cover {
    position: absolute;
    left: 221px;
    top: 31px;
    width: 758px;
    height: 1137px;
    background: radial-gradient(ellipse 62% 48% at 50% 50%, var(--cover-glow) 0%, var(--cover-mid) 55%, var(--cover-edge) 100%);
    overflow: hidden;
    color: var(--ink-cream);
  }
  .cover__artwork {
    position: absolute;
    left: 186px;
    top: 398px;
    width: 385px;
    height: 316px;
    background: radial-gradient(ellipse at 55% 45%, var(--sketch-tint) 0%, rgba(248, 211, 212, 0) 70%);
  }
  .cover__title {
    position: absolute;
    left: 0;
    right: 0;
    top: 96px;
    margin: 0;
    text-align: center;
    font-family: "EB Garamond", Garamond, serif;
    font-weight: 400;
    font-size: 124px;
    line-height: 110px;
    letter-spacing: 2px;
    text-transform: uppercase;
  }
  .cover__title span { display: block; }
  .cover__subtitle {
    position: absolute;
    left: 158px;
    width: 453px;
    top: 696px;
    padding: 14px 0 16px;
    border-top: 1px solid var(--rule-gold);
    border-bottom: 1px solid var(--rule-gold);
    margin: 0;
    text-align: center;
    font-family: "Cormorant Garamond", Garamond, serif;
    font-style: italic;
    font-weight: 500;
    font-size: 54px;
    line-height: 60px;
  }
  .cover__author {
    position: absolute;
    left: 0;
    right: 0;
    top: 948px;
    margin: 0;
    text-align: center;
    font-family: "EB Garamond", Garamond, serif;
    font-weight: 500;
    font-size: 48px;
    line-height: 52px;
    letter-spacing: 4px;
    text-transform: uppercase;
  }
  .cover__author span { display: block; }
</style>
</head>
<body>
  <main class="canvas">
    <section class="cover">
      <div class="cover__artwork" role="img" aria-label="Faint line sketch of a house under construction"></div>
      <h1 class="cover__title">
        <span>Under</span>
        <span>The</span>
        <span>Quiet</span>
        <span>Sky</span>
      </h1>
      <p class="cover__subtitle">A Gardener’s Notes on<br>Patience</p>
      <p class="cover__author">
        <span>Tobias</span>
        <span>Quellhorst</span>
      </p>
    </section>
  </main>
</body>
</html>
```